Beauty Salon Industry - Web Design Project

zQuarta is a well-funded start up developing an Online Marketing Platform for small businesses in Europe.
We require a large number of high quality business web designs for our business website builder. Our business websites are seamlessly integrated into our Online Marketing systems and therefore it is important for designers to comply with our Design Guidelines.
This is our second contest and it will focus on the beauty salon industry. We will be running contents every 2-3 weeks for a new industry. Last month, we ran a contest for Builder website designs with 3 top prizes (plus £10 per variation) and we also paid out £25 per design for 20+ entries from designers who did not win the top prizes. So we encourage all entries!
We have included a wire frame this time to encourage you to be as creative as possible with your designs and layout while respecting the following guidelines:
1) You CAN change the layout as much as you like. If you think a vertical menu would look better, then use it. If you think the design would benefit from moving an element to a different location, then you can do that too.
2) You must include ALL the elements in the wire frame in your design.(e.g. latest 2 news entries, a testimonial, 1 gallery image, carousel etc...). Please make sure you have looked through the wire frame and know what is required. Entries that do not include all the elements will not qualify to win.
3) So remember, you CAN change the layout as much as you like but DO NOT remove any elements nor move them to a different page.
4) You may change the size and style of the carousel image. We would like to see as many variations of this as possible.
We are rewarding 3 prizes, and would like the winning designer to design the internal pages to the new design.
As always, if we think your designs could be incorporated into our system, but you do not win the competition, we will reward £25. Therefore, we encourage designers to submit as many designs as possible as we may award up to 25 designs.
Judging criteria : -
1) Visual Design
2) Layout must adhere to best practices and wireframe. If you decide to move elements around significantly please provide reason
3) Functional, informative and drives calls to action
Updates
As usual:
1st place = £350
2nd place = £250
3rd place = £150
Good luck!
Very happy with all the designs submitted so far, and will provide feedback ASAP.
We would like to see you try arranging the elements differently. So please try different navigation types and layouts.
Thanks
Morris
Prize funds for 1st place has been slightly increased.
Thanks
Morris
We have already had some amazing designs submitted. Thanks.
Remember to play with the layout of the elements and try designs with a carousel/slider that is in portrait not just in landscape.
Thanks everyone!
Morris
Hi everyone, we are really enjoying looking through the designs.
We have one NEW requirement. If you have used an image from http://www.frelik-example.com/ in your design, could you please replace it with another.
We are not associated with them.
Thank you.
I have just sent a poll around the office to vote on all the designs and hope to have the results soon.
Good luck and I hope to see all your great designs for our next project in a couple of weeks.
Morris
Hi everyone, we hope you have had a good holiday season. We will be rewarding the prizes very soon, hopefully today or tomorrow.
Thanks
Morris
We are currently going through all the designs that did not win our competition and will be contacting the designers of the designs we would like to use in our system, so please keep an eye on your inbox over the next few days.
Thank you
Morris
Target Market(s)
Beauty Salon Industry
Industry/Entity Type
Beauty Salon
Look and feel
Each slider illustrates characteristics of the customer's brand and the style your logo design should communicate.

```html
<!DOCTYPE html>
<html lang="en">
<head>
<meta charset="utf-8">
<title>Lumen Loft – Hair and Urban Spa</title>
<link rel="stylesheet" href="https://fonts.googleapis.com/css2?family=Lora:ital,wght@0,400;0,700;1,400&family=Noto+Serif:wght@400;700&family=Arimo:ital,wght@0,400;0,700;1,400&display=swap">
<style>
:root{
  --plum-deep:#1d0f2c;
  --plum:#2e1a47;
  --plum-btn:#3a2150;
  --page:#e9eaee;
  --panel:#f3f4f7;
  --ink:#333;
  --ink-soft:#555;
  --steel:#7c8aa3;
  --link:#1a8fe0;
  --rule:#cfd2d8;
  --white:#fff;
}
*{box-sizing:border-box;margin:0;padding:0}
html,body{width:1200px;height:1185px;overflow:hidden}
body{position:relative;background:linear-gradient(#eef0f3,#e4e6ea);font-family:"Noto Serif",Georgia,serif;color:var(--ink)}
.abs{position:absolute}
.header{left:0;top:0;width:1200px;height:189px;background:radial-gradient(ellipse at 55% 0%,#4a2a6a 0%,var(--plum) 45%,var(--plum-deep) 100%)}
.brand{left:160px;top:52px;display:flex;align-items:center;gap:12px}
.brand-mark{width:40px;height:40px;border-radius:50%;background:#e8e4ee}
.brand-name{font-family:"Lora",serif;font-size:44px;font-weight:700;color:#f4f2f7;line-height:1}
.brand-tag{left:229px;top:117px;font-family:"Lora",serif;font-style:italic;font-size:27px;color:#d9d3e2;letter-spacing:.5px}
.booking{left:799px;top:110px;width:259px;height:39px;border-radius:6px;background:linear-gradient(#fff,#e3e4e8);display:flex;align-items:center;font-family:"Arimo",sans-serif;white-space:nowrap}
.booking-phone{padding-left:11px;padding-right:6px;font-size:19px;line-height:1;color:#2a2038;letter-spacing:-.6px}
.booking-cta{flex:1;height:29px;margin-right:5px;border-radius:4px;background:linear-gradient(#e9eaef,#cfd2da);color:#7a88a2;font-weight:700;font-size:18px;line-height:1;display:flex;align-items:center;justify-content:center;letter-spacing:.5px}
.nav{left:158px;top:169px;width:900px;height:39px;border-radius:5px;background:linear-gradient(#fff,#e6e7ea);box-shadow:0 2px 3px rgba(0,0,0,.15);display:flex;align-items:center;padding-left:7px;font-size:14px;white-space:nowrap}
.nav a{text-decoration:none;color:#222;height:39px;display:flex;align-items:center;padding:0 22px;border-right:1px solid #d7d8dc}
.nav a.current{background:var(--plum);color:#fff;height:30px;border-radius:4px;padding:0 14px;margin-right:9px;border:0}
.nav a:last-child{border-right:0}
.intro{left:158px;top:250px;width:208px}
.intro h1{font-family:"Lora",serif;font-weight:400;font-size:22px;line-height:27px;color:#3a3a3a}
.intro p{font-size:11px;line-height:17px;text-align:justify;margin-top:17px;color:#333}
.btn{display:inline-flex;align-items:center;justify-content:center;background:var(--plum-btn);color:#fff;font-family:"Arimo",sans-serif;font-size:14px;border-radius:4px;box-shadow:0 1px 2px rgba(0,0,0,.35);white-space:nowrap}
.rule{height:1px;background:var(--rule)}
.gallery-frame{left:155px;top:588px;width:206px;height:268px;background:#fff;padding:3px;box-shadow:0 1px 4px rgba(0,0,0,.2)}
.fill{width:100%;height:100%}
.slider{left:385px;top:254px;width:434px;height:286px;box-shadow:0 6px 8px -4px rgba(0,0,0,.35)}
.slider-photo{background:radial-gradient(ellipse at 60% 35%,#7a3ea0 0%,#5b5b5b 35%,#3a3a3a 100%)}
.slider-arrows{left:15px;top:246px;display:flex;gap:6px}
.slider-arrows svg{display:block}
.quote{left:385px;top:562px;width:434px;font-family:"Lora",serif;font-style:italic;font-size:20px;line-height:27px;color:#444;text-align:justify}
.quote-by{left:385px;top:643px;width:414px;text-align:right;font-family:"Lora",serif;font-style:italic;font-size:16px;color:#555}
.news{top:740px;width:208px}
.news h2{font-family:"Lora",serif;font-weight:400;font-size:17.5px;color:var(--link);white-space:nowrap}
.news p{font-size:10.3px;line-height:17px;margin-top:8px;text-align:justify;height:52px;letter-spacing:-.1px}
.news a{color:var(--link);text-decoration:none}
.news-meta{display:flex;justify-content:space-between;align-items:center;font-size:11px;margin-top:16px;white-space:nowrap}
.news-meta span.by{display:flex;align-items:center;gap:6px;color:var(--link)}
.card{background:var(--panel);border-radius:5px;box-shadow:0 0 4px rgba(0,0,0,.12)}
.offer{left:834px;top:249px;width:216px;height:272px}
.offer-product{left:48px;top:18px;width:126px;height:100px;border-radius:3px;background:linear-gradient(#f7f7f8,#d8d9dc)}
.offer-price{left:24px;top:137px;font-family:"Arimo",sans-serif;font-weight:700;font-size:40px;color:#7c8aa3;letter-spacing:-1px}
.offer-line{left:12px;top:180px;width:196px}
.offer-text{left:16px;top:193px;font-family:"Arimo",sans-serif;font-size:16px;line-height:21px;color:#8790a2;white-space:nowrap}
.offer-cta{left:16px;top:241px;font-family:"Arimo",sans-serif;font-size:17px;color:#7c8aa3;white-space:nowrap}
.info{left:834px;top:542px;width:216px;height:317px;font-family:"Arimo",sans-serif}
.label{background:var(--plum);color:#fff;font-size:13.5px;width:122px;height:22px;border-radius:4px;display:flex;align-items:center;padding-left:13px;white-space:nowrap}
.info address{font-style:normal;font-size:13px;line-height:16px;color:#7c8396}
.map-link{font-style:italic;font-size:12px;color:var(--link);white-space:nowrap}
.hours{font-size:13px;color:#8a90a0;border-collapse:collapse;white-space:nowrap}
.hours td{height:18.7px;padding:0}
.hours td+td{color:var(--link);padding-left:0}
.partners{left:158px;top:951px;width:900px;height:114px;display:flex;justify-content:space-between;align-items:center}
.partner{font-family:"Noto Serif",serif;font-size:24px;color:#1a1a1a;white-space:nowrap}
.partner.box{background:#050505;color:#fff;width:182px;height:113px;display:flex;align-items:center;justify-content:center;font-size:18px;text-align:center;line-height:24px;white-space:normal}
.footer{left:0;top:1077px;width:1200px;height:108px;background:var(--plum);font-family:"Arimo",sans-serif}
.footer-copy{left:157px;top:24px;font-size:11px;color:#e6e2ec;letter-spacing:.4px;white-space:nowrap}
.footer-brand{left:831px;top:22px;display:flex;align-items:center;gap:8px;color:#6e6082;white-space:nowrap}
.footer-brand .brand-mark{width:28px;height:28px;background:#5f5175}
.footer-brand b{font-family:"Lora",serif;font-size:30px}
.footer-tag{left:873px;top:66px;font-family:"Lora",serif;font-style:italic;font-size:17px;color:#6e6082;white-space:nowrap}
</style>
</head>
<body>

<header class="header abs">
  <div class="brand abs"><span class="brand-mark"></span><span class="brand-name">Lumen Loft</span></div>
  <div class="brand-tag abs">Hair and Urban Spa</div>
  <div class="booking abs"><span class="booking-phone">020 7946 0182</span><span class="booking-cta">BOOK NOW</span></div>
</header>

<nav class="nav abs">
  <a class="current" href="#">HOME</a>
  <a href="#">SERVICES</a>
  <a href="#">GALLERY</a>
  <a href="#">TESTIMONIALS</a>
  <a href="#">NEWS</a>
  <a href="#">ABOUT US</a>
  <a href="#">CONTACT US</a>
</nav>

<section class="intro abs">
  <h1>LET OUR HAIR AND BEAUTY SKILLS BLOW YOU AWAY</h1>
  <p>Lumen Loft is a passionate, creative team, dedicated to delivering a second to none, personal salon experience that will ‘blow’ your mind</p>
  <p>Where ultimate hairdressing comes hand-in-hard with style, glamour, fashion, innovation and skill to create an exquisite salon experience in the heart of London.</p>
</section>
<span class="btn abs" style="left:278px;top:527px;width:78px;height:21px">More</span>
<div class="rule abs" style="left:165px;top:561px;width:196px"></div>

<figure class="gallery-frame abs">
  <div class="fill" role="img" aria-label="Gallery photo of a model with short auburn hair and a fur collar" style="background:radial-gradient(ellipse at 45% 35%,#8a6a5a 0%,#4f5a52 45%,#2e3530 100%)"></div>
</figure>
<span class="btn abs" style="left:274px;top:874px;width:86px;height:20px">View Gallery</span>

<section class="slider abs">
  <div class="fill slider-photo" role="img" aria-label="Carousel photo of a woman with vivid purple hair lying on a grey surface"></div>
  <div class="slider-arrows abs">
    <svg width="15" height="15" viewBox="0 0 15 15"><circle cx="7.5" cy="7.5" r="7" fill="#e6e6e6"/><path d="M9 4 5.5 7.5 9 11" stroke="#333" stroke-width="1.8" fill="none"/></svg>
    <svg width="15" height="15" viewBox="0 0 15 15"><circle cx="7.5" cy="7.5" r="7" fill="#e6e6e6"/><path d="M6 4l3.5 3.5L6 11" stroke="#333" stroke-width="1.8" fill="none"/></svg>
  </div>
</section>

<blockquote class="quote abs">“My hairstylist, Elodie, was truly amazing. She listened to exactly what i wanted, but also told me exactly what....”</blockquote>
<div class="quote-by abs">- Mira Castell -</div>
<span class="btn abs" style="left:726px;top:680px;width:77px;height:21px">More</span>
<div class="rule abs" style="left:395px;top:720px;width:414px"></div>

<article class="news abs" style="left:384px">
  <h2>Book Now for Christmas</h2>
  <p>Our salon is usually very busy for the two weeks before Christmas, so please book early: call <a href="#">020 7946 0182</a>, or contact us.</p>
  <div class="news-meta"><span>1 Dec, 2011</span><span class="by"><svg width="18" height="16" viewBox="0 0 18 16"><path d="M9 1C4.5 1 1 3.8 1 7.2c0 2 1.2 3.7 3 4.8L3 15l4-2.2c.6.1 1.3.2 2 .2 4.5 0 8-2.8 8-6.3S13.5 1 9 1z" fill="#bfe0f6" stroke="#8cc2e6"/></svg>By. Admin</span></div>
</article>
<article class="news abs" style="left:609px">
  <h2>Want to be a hair model?</h2>
  <p>We always need models for our portfolio. If you want to become one, please contact us.</p>
  <div class="news-meta"><span>9 Dec, 2011</span><span class="by"><svg width="18" height="16" viewBox="0 0 18 16"><path d="M9 1C4.5 1 1 3.8 1 7.2c0 2 1.2 3.7 3 4.8L3 15l4-2.2c.6.1 1.3.2 2 .2 4.5 0 8-2.8 8-6.3S13.5 1 9 1z" fill="#bfe0f6" stroke="#8cc2e6"/></svg>By. Admin</span></div>
</article>
<span class="btn abs" style="left:556px;top:881px;width:78px;height:20px">More news</span>

<aside class="offer card abs">
  <div class="offer-product abs" role="img" aria-label="Photo of a stack of styling product boxes"></div>
  <div class="offer-price abs">£ 25</div>
  <div class="offer-line rule abs"></div>
  <div class="offer-text abs">Complimentary gift<br>for first-time clients!</div>
  <div class="offer-cta abs">Book Appointment Now</div>
</aside>

<aside class="info card abs">
  <div class="label abs" style="left:13px;top:11px">Salon Address</div>
  <div class="rule abs" style="left:13px;top:40px;width:190px"></div>
  <address class="abs" style="left:16px;top:54px">12 Ashgrove Lane<br>London<br>W2 4QT</address>
  <span class="map-link abs" style="left:121px;top:107px">View Map &nbsp;&gt;</span>
  <div class="abs" style="left:8px;top:134px;width:200px;border-top:1px dotted #9aa3b3"></div>
  <div class="label abs" style="left:13px;top:146px">Business Hour</div>
  <div class="rule abs" style="left:13px;top:175px;width:190px"></div>
  <table class="hours abs" style="left:16px;top:189px">
    <tr><td style="width:88px">Mon.</td><td>9 a.m - 5 p.m</td></tr>
    <tr><td>Tue.</td><td>9 a.m - 5 p.m</td></tr>
    <tr><td>Wed.</td><td>9 a.m - 5 p.m</td></tr>
    <tr><td>Thu.</td><td>9 a.m - 5 p.m</td></tr>
    <tr><td>Fri.</td><td>9 a.m - 5 p.m</td></tr>
    <tr><td>Sat.</td><td>9 a.m - 5 p.m</td></tr>
  </table>
</aside>

<div class="rule abs" style="left:185px;top:921px;width:840px"></div>

<section class="partners abs">
  <span class="partner">MAISON VEREL</span>
  <span class="partner" style="color:#c8103e">CORVANE</span>
  <span class="partner">Tillery &amp; Co</span>
  <span class="partner box">Halberg<br>Professional</span>
</section>

<footer class="footer abs">
  <div class="footer-copy abs">Copyright © 2011 LUMEN LOFT limited. All rights reserved. &nbsp;Managed by zQuarta.com &nbsp; I &nbsp; Admin</div>
  <div class="footer-brand abs"><span class="brand-mark"></span><b>Lumen Loft</b></div>
  <div class="footer-tag abs">Hair and Urban Spa</div>
</footer>

</body>
</html>
```